Brochure Design Project

I need a brochure design for a full Hair Salon, located in Rockville MD called Corvetta Hair, Nails and Spa.
Please use inovative design (the idea is to target an audience between the age of 19 to 50) keeping our main colors (spring green, grey and white).
we would also like to include the list of services which will be provided when needed.

Target Market(s)

women between 19 to 50 - all ethnical backgrounds

Industry/Entity Type

Hair

Requirements
Nice to have
• we would like to include a blurb, contact info and list of prices of all the services we provided. Also we would like to add the line "se habla espaƱol" anywhere in the brochure.

```html
<!DOCTYPE html>
<html lang="en">
<head>
<meta charset="utf-8">
<title>Corvetta Hair, Nails and Spa – Brochure</title>
<link rel="stylesheet" href="https://fonts.googleapis.com/css2?family=Questrial&display=swap">
<style>
  :root {
    --spring-green: #c9dc78;
    --salon-grey: #8e8f93;
    --paper: #ffffff;
    --ink: #1f1f1f;
    --soft-white: #f2f2f2;
    --silver-light: #f4f4f4;
    --silver-dark: #9a9a9a;
  }
  html, body {
    margin: 0;
    padding: 0;
    width: 1200px;
    height: 935px;
    overflow: hidden;
    background: var(--paper);
  }
  .brochure {
    position: relative;
    width: 1200px;
    height: 935px;
    background: var(--paper);
    font-family: "Questrial", "Century Gothic", sans-serif;
    color: var(--ink);
  }
  .about-panel {
    position: absolute;
    left: 21px; top: 21px;
    width: 383px; height: 600px;
    background: var(--spring-green);
  }
  .about-heading {
    position: absolute;
    left: 40px; top: 49px;
    width: 303px; height: 41px;
    background: linear-gradient(90deg, var(--silver-dark) 0%, var(--silver-light) 35%, var(--silver-light) 70%, var(--silver-dark) 100%);
    box-shadow: 0 3px 4px rgba(0,0,0,0.25);
    font-size: 21px;
    line-height: 41px;
    text-align: center;
    color: #222;
  }
  .about-copy {
    position: absolute;
    left: 28px; top: 124px;
    width: 327px;
    text-align: center;
    font-size: 17px;
    line-height: 17.8px;
    color: #1a1a1a;
  }
  .about-copy p { margin: 0 0 18px; }
  .salon-photo {
    position: absolute;
    left: 21px; top: 621px;
    width: 383px; height: 291px;
    background: linear-gradient(160deg, #e7b45a 0%, #c98a3a 45%, #6e4a22 100%);
  }
  .feature-panel {
    position: absolute;
    left: 404px; top: 21px;
    width: 774px; height: 891px;
    background: var(--salon-grey);
    overflow: hidden;
  }
  .feature-panel svg { position: absolute; left: 0; top: 0; }
  .intro {
    position: absolute;
    left: 37px; top: 84px;
    width: 310px;
    margin: 0;
    font-size: 14px;
    line-height: 17px;
    color: var(--soft-white);
  }
  .wordmark {
    position: absolute;
    color: var(--spring-green);
    line-height: 1;
  }
  .wordmark-top { left: 437px; top: 78px; font-size: 58px; }
  .wordmark-top span, .wordmark-bottom span { display: block; font-size: 0.29em; letter-spacing: 1px; margin-top: 6px; text-align: right; }
  .wordmark-bottom { left: 47px; top: 652px; font-size: 42px; }
  .contact {
    position: absolute;
    left: 37px; top: 728px;
    margin: 0;
    font-size: 14px;
    line-height: 17px;
    color: var(--soft-white);
    font-style: normal;
  }
  .contact span { display: block; margin-bottom: 12px; }
  .spanish-band {
    position: absolute;
    left: 815px; top: 799px;
    width: 363px; height: 41px;
    background: var(--spring-green);
    box-shadow: -3px 3px 4px rgba(0,0,0,0.35);
    font-size: 26px;
    line-height: 41px;
    padding-left: 30px;
    box-sizing: border-box;
    color: #1a1a1a;
  }
</style>
</head>
<body>
<main class="brochure">
  <section class="about-panel">
    <h2 class="about-heading" style="margin:0;font-weight:normal;">About Us</h2>
    <div class="about-copy">
      <p>Corvetta Hair, Nails and Spa was founded by Lucía Ferreira and Valeria Ferreira. Aside from being a mother and daughter, they are both professionals with the vision of providing the Washington metropolitan area, beauty services of the highest quality within a cheerful, relaxing, and friendly environment.</p>
      <p>Lucía Ferreira, originally from Colombia, South America, is an experienced beauty professional passionate about her work, with over 25 years of experience in the beauty industry.</p>
      <p>Our international staff has a long history of providing excellent customer service, and will help to find the look that's right for you. When you visit, you will feel as if you were at home.</p>
    </div>
  </section>

  <div class="salon-photo" role="img" aria-label="Photo of a warmly lit salon treatment room with a spa bed and product shelves"></div>

  <section class="feature-panel">
    <svg width="774" height="891" viewBox="0 0 774 891" aria-hidden="false">
      <circle cx="384" cy="444" r="255" fill="#ffffff"/>
      <defs>
        <radialGradient id="portrait-tones" cx="55%" cy="60%" r="60%">
          <stop offset="0%" stop-color="#e8c2ae"/>
          <stop offset="45%" stop-color="#b58a7a"/>
          <stop offset="75%" stop-color="#2a2626"/>
          <stop offset="100%" stop-color="#0d0d0d"/>
        </radialGradient>
      </defs>
      <circle cx="343" cy="442" r="243" fill="url(#portrait-tones)" role="img" aria-label="Portrait of a model with a glossy black bob haircut"/>
    </svg>

    <p class="intro">We specialize in providing a pleasant experience for all the family members in need of full service beauty salon with very affordable prices.</p>

    <div class="wordmark wordmark-top">Corvetta<span>HAIR, NAILS AND SPA</span></div>
    <div class="wordmark wordmark-bottom">Corvetta<span>HAIR, NAILS AND SPA</span></div>

    <address class="contact">
      <span>4820 Linden Court, Rockville,<br>Maryland 20850</span>
      <span>+1 301-555-0148</span>
      <span>lucia@corvettasalon.com</span>
      <span>www.corvettahns.com</span>
    </address>
  </section>

  <div class="spanish-band">se habla español</div>
</main>
</body>
</html>
```